A design led business card for the construction industry

High-end business card to match logo. White logo on dark grey/off black to the front. Matching dark font on white to back, possibly with logo design again.

We offer construction and project management services to commercial and private clients in the UK. Projetcs range from newbuilds, conversion of listed buildings and refurbishments and extensions of existing homes. Our focus is on quality and attention to detail using the highest skills.

Contact Information for Business Card

Name; Dorian Hatch BSc
Position; Project Manager
Mobile; 07962 804 157
Tel; 01632 958412
email; dorian@framelark.co.uk
web; www.framelark.co.uk
Address; Kelbury on Wold, KT4 7PZ

Colors

Designer to choose only greyscale colors for use in the design.

Requirements
Must have
• To include the below description of the business,

CONSTRUCTION - PROJECT MANAGEMENT
Nice to have
• The posibility of the top back of the card being used as a ruler. So will have a measurement to scale in mm or an architect scale of 1:50
Should not have
• Should not be portrait

```html
<!DOCTYPE html>
<html lang="en">
<head>
<meta charset="utf-8">
<title>Framelark – Business Card</title>
<link href="https://fonts.googleapis.com/css2?family=Roboto:wght@300;400;500&display=swap" rel="stylesheet">
<style>
  :root {
    --stage: #e3e3e3;
    --card-dark: #2b2a29;
    --card-light: #f4f4f4;
    --ink: #2b2a29;
    --ink-soft: #3a3a3a;
    --white: #ffffff;
  }
  html, body {
    margin: 0;
    width: 1200px;
    height: 960px;
    overflow: hidden;
    background: var(--stage);
    font-family: "Roboto", Arial, sans-serif;
  }
  .canvas { position: relative; width: 1200px; height: 960px; }
  .card {
    position: absolute;
    left: 328px;
    width: 544px;
    height: 350px;
    box-sizing: border-box;
  }
  /* Front */
  .card-front { top: 110px; background: var(--card-dark); color: var(--white); }
  .front-name {
    position: absolute; left: 0; right: 0; top: 232px;
    text-align: center;
    font-weight: 300; font-size: 34px; letter-spacing: 12px;
    text-indent: 12px;
  }
  .front-tagline {
    position: absolute; left: 0; right: 0; top: 307px;
    text-align: center;
    font-weight: 400; font-size: 15px; letter-spacing: 0.2px;
  }
  /* Back */
  .card-back { top: 503px; background: var(--card-light); color: var(--ink); }
  .ruler { position: absolute; left: 0; top: 0; }
  .ruler-label { font-family: "Roboto", Arial, sans-serif; font-size: 10px; fill: var(--ink); }
  .back-name {
    position: absolute; left: 39px; top: 143px;
    font-weight: 300; font-size: 22px; letter-spacing: 7px; color: var(--ink);
  }
  .person {
    position: absolute; right: 40px; top: 153px; text-align: right;
  }
  .person-name { font-weight: 500; font-size: 20px; line-height: 24px; color: var(--ink); }
  .person-role { font-weight: 400; font-size: 15px; line-height: 18px; color: var(--ink-soft); }
  .address {
    position: absolute; left: 39px; top: 215px;
    font-size: 16px; color: var(--ink-soft);
  }
  .contacts {
    position: absolute; left: 39px; top: 240px;
    margin: 0; padding: 0; list-style: none;
    font-size: 16px; line-height: 19px; color: var(--ink-soft);
  }
  .contacts li { display: flex; align-items: center; gap: 5px; }
  .contacts svg { width: 13px; height: 13px; flex: none; }
</style>
</head>
<body>
<main class="canvas">

  <section class="card card-front" aria-label="Card front">
    <div class="front-name">FRAMELARK</div>
    <div class="front-tagline">CONSTRUCTION - PROJECT MANAGEMENT</div>
  </section>

  <section class="card card-back" aria-label="Card back">
    <svg class="ruler" width="544" height="40" viewBox="0 0 544 40" aria-label="1:50 scale ruler">
      <defs>
        <pattern id="tick-minor" patternUnits="userSpaceOnUse" x="33" y="0" width="12.8" height="40">
          <rect x="0" y="0" width="1" height="16" fill="#2b2a29"/>
        </pattern>
        <pattern id="tick-half" patternUnits="userSpaceOnUse" x="33" y="0" width="64" height="40">
          <rect x="0" y="0" width="1" height="24" fill="#2b2a29"/>
        </pattern>
        <pattern id="tick-metre" patternUnits="userSpaceOnUse" x="33" y="0" width="128" height="40">
          <rect x="0" y="0" width="1" height="36" fill="#2b2a29"/>
        </pattern>
      </defs>
      <rect x="33" y="0" width="500" height="18" fill="url(#tick-minor)"/>
      <rect x="33" y="0" width="500" height="26" fill="url(#tick-half)"/>
      <rect x="33" y="0" width="500" height="38" fill="url(#tick-metre)"/>
      <text class="ruler-label" x="6" y="37">1:50</text>
      <text class="ruler-label" x="165" y="37">1m</text>
      <text class="ruler-label" x="293" y="37">2m</text>
      <text class="ruler-label" x="421" y="37">3m</text>
    </svg>

    <div class="back-name">FRAMELARK</div>

    <div class="person">
      <div class="person-name">Dorian Hatch BSc</div>
      <div class="person-role">Project Manager</div>
    </div>

    <div class="address">Kelbury on Wold, KT4 7PZ</div>

    <ul class="contacts">
      <li>
        <svg viewBox="0 0 13 13" aria-hidden="true"><rect x="3.5" y="0.8" width="6" height="11.4" rx="1" fill="none" stroke="#2b2a29" stroke-width="1.2"/><line x1="5.5" y1="10" x2="7.5" y2="10" stroke="#2b2a29"/></svg>
        07962 804 157
      </li>
      <li>
        <svg viewBox="0 0 13 13" aria-hidden="true"><path d="M2.5 1 L5 1 L6 3.8 L4.6 5 C5.4 6.8 6.3 7.7 8 8.5 L9.2 7 L12 8 L12 10.6 C12 11.4 11.4 12 10.6 12 C5.6 11.6 1.5 7.5 1 2.4 C1 1.6 1.7 1 2.5 1 Z" fill="#2b2a29"/></svg>
        01632 958412
      </li>
      <li>
        <svg viewBox="0 0 13 13" aria-hidden="true"><rect x="0.8" y="2.5" width="11.4" height="8" fill="none" stroke="#2b2a29" stroke-width="1.1"/><path d="M0.8 2.5 L6.5 7 L12.2 2.5" fill="none" stroke="#2b2a29" stroke-width="1.1"/></svg>
        dorian@framelark.co.uk
      </li>
      <li>
        <svg viewBox="0 0 13 13" aria-hidden="true"><circle cx="6.5" cy="6.5" r="5.6" fill="none" stroke="#2b2a29" stroke-width="1"/><ellipse cx="6.5" cy="6.5" rx="2.4" ry="5.6" fill="none" stroke="#2b2a29" stroke-width="0.9"/><line x1="0.9" y1="6.5" x2="12.1" y2="6.5" stroke="#2b2a29" stroke-width="0.9"/></svg>
        www.framelark.co.uk
      </li>
    </ul>
  </section>

</main>
</body>
</html>
```